Seniors Massage Care Business Needs a New Website

Hello,
We require a website to be designed and coded. The design and coding must be high quality. Our website host has requested files be in static HTML format if possible.

The business is a mobile massage service for seniors (elderly people). The designer should emphasise that the business is a mobile service

The website will only have 4 pages.

1. Home- very simple layout and minimal information
2. Massage Services- this houses all of the information about the different services etc.
3. Contact Us-
4. ホーム (this is the Japanese symbol for 'home')- All of the information on the home page (section 1) will be translated into Japanese and uploaded to the brief for the designers to insert.

There is no requirement for an online booking, just contact information. The words 'Make a Booking' can be used and should lead customers to the 'Contact Us' page.

I have attached the business logo in multiple formats for designers to use.

I will upload more content and images to use for the website by the end of this week.

Thank you. I look forward to working with the successful candidate.

Target Market(s)

People aged 50+ years

Industry/Entity Type

Massage Therapy

Coding

Coded - Design and coding required

Number of Pages Required

4 page

Font styles to use
Sans Serif

Colors
74cabd
abd036
9ccb3b
f6faec
ffffff

Requirements
Must have
• Copyright free images and photos that we have taken. Both are important.
• Simple and inviting design.
Nice to have
• Colours of the logo incorporated.
Should not have
• This business is not a massage shop, so no images of massage shops or day salons required.
• Not too much imagery as the design needs to be simple.

```html
<!DOCTYPE html>
<html lang="en">
<head>
<meta charset="utf-8">
<title>Silver Touch Mobile Massage — Home</title>
<link rel="stylesheet" href="https://fonts.googleapis.com/css2?family=Josefin+Sans:wght@400;600&family=Raleway:wght@400;600&family=Noto+Sans+JP:wght@400&display=swap">
<style>
:root{
  --green:#9ccb3b;
  --green-lime:#abd036;
  --teal:#74cabd;
  --cream:#f6faec;
  --band:#eef5de;
  --white:#ffffff;
  --ink:#2a2a2a;
  --muted:#555;
}
*{margin:0;padding:0;box-sizing:border-box}
html,body{width:1200px;height:2177px;overflow:hidden}
body{position:relative;background:var(--cream);font-family:"Raleway",sans-serif;color:var(--ink)}
.abs{position:absolute}
.site-header{left:0;top:0;width:1200px;height:186px;background:var(--white)}
.brand{display:flex;flex-direction:column;align-items:center;color:var(--green);font-family:"Josefin Sans",sans-serif;font-weight:400;text-align:center;white-space:nowrap}
.brand-mark{width:50px;height:50px;border:3px solid var(--green);border-radius:50%;margin-bottom:10px}
.brand-name{font-size:24px;letter-spacing:.5px;line-height:1.1;padding:0 6px 4px;border-bottom:1px solid var(--green)}
.brand-sub{font-size:12px;letter-spacing:5px;margin-top:3px;color:var(--muted)}
.header-brand{left:68px;top:16px;width:280px}
.contact-item{display:flex;align-items:center;gap:12px;font-size:13px;line-height:18px;color:var(--ink);white-space:nowrap}
.contact-item svg{width:34px;height:34px}
.call{left:784px;top:22px}
.mail{left:949px;top:22px}
.nav{display:flex;font-family:"Josefin Sans","Noto Sans JP",sans-serif;font-size:17px;letter-spacing:2px;white-space:nowrap}
.nav a{color:var(--ink);text-decoration:none;position:relative;white-space:nowrap}
.nav a.active{color:var(--green)}
.nav .jp{font-family:"Noto Sans JP",sans-serif;font-size:15px;letter-spacing:1px}
.main-nav{top:91px;right:53px;gap:56px}
.main-nav a.active::after{content:"";position:absolute;left:0;right:0;bottom:-9px;height:2px;background:var(--green)}
.hero{left:68px;top:135px;width:1079px;height:454px;background:linear-gradient(100deg,#dfe6df 0%,#4e7a3a 20%,#6f9a4d 45%,#c9cfc4 70%,#e9e6df 100%);box-shadow:0 22px 26px -16px rgba(0,0,0,.35)}
.hero-caption{left:0;right:0;top:290px;text-align:center;color:var(--white);font-family:"Josefin Sans",sans-serif;font-size:23px;line-height:29px;letter-spacing:.5px;text-shadow:0 1px 3px rgba(0,0,0,.5)}
.hero-arrow{top:205px;width:36px;height:42px;background:rgba(255,255,255,.75);display:flex;align-items:center;justify-content:center}
.hero-arrow.prev{left:0}.hero-arrow.next{right:0}
.about-photo{left:68px;width:362px;height:273px;border:4px solid var(--white);border-radius:8px;box-shadow:0 0 0 1px #ddd}
.photo-one{top:670px;background:linear-gradient(90deg,#d8d0c4,#3a5aa8 35%,#efe9e1 55%,#222 75%,#d8d0c4)}
.photo-two{top:966px;background:linear-gradient(90deg,#d9cfc2,#e9dcd0 35%,#8bb7b3 55%,#2b2b2b 80%,#d9cfc2)}
.about{left:472px;top:664px;width:675px}
.section-title{font-family:"Josefin Sans",sans-serif;font-weight:400;font-size:29px;letter-spacing:2.5px;color:var(--ink);white-space:nowrap}
.section-title span{color:var(--green)}
.about .section-title{font-size:27px;letter-spacing:1.5px;padding-bottom:10px;border-bottom:1px dotted #9aa;margin-bottom:18px}
.about p{font-size:14px;line-height:22px;color:var(--ink);margin-bottom:8px}
.about h3{font-size:14px;font-weight:600;line-height:22px}
.btn{display:inline-block;margin-top:22px;background:var(--green);color:var(--white);font-family:"Josefin Sans",sans-serif;font-size:18px;padding:13px 18px 11px;border-radius:3px;text-decoration:none}
.services{left:0;top:1302px;width:1200px;height:533px;background:var(--band)}
.services .section-title{position:absolute;left:0;right:0;top:52px;text-align:center;font-size:37px}
.title-rule{left:326px;top:106px;width:547px;border-top:1px dotted #8a9}
.title-rule::after{content:"";position:absolute;left:148px;top:-4px;width:251px;height:6px;background:var(--green)}
.service{top:149px;width:260px;text-align:center}
.service-photo{width:215px;height:215px;border-radius:50%;margin:0 auto 26px}
.service h3{font-family:"Josefin Sans",sans-serif;font-weight:400;font-size:23px;letter-spacing:1.5px;margin-bottom:10px}
.service p{font-size:13px;line-height:19px;color:var(--ink)}
.service a{display:block;margin-top:14px;color:var(--green);font-family:"Josefin Sans",sans-serif;font-size:16px;letter-spacing:.5px;text-decoration:none}
.site-footer{left:0;top:1835px;width:1200px;height:295px;background:var(--cream)}
.footer-brand{left:420px;top:34px;width:360px}
.footer-nav{top:198px;left:0;right:0;justify-content:center;gap:56px}
.socials{top:259px;left:559px;display:flex;gap:8px}
.socials span{width:22px;height:22px;border-radius:50%}
.copyright{left:0;top:2130px;width:1200px;height:47px;background:var(--green);color:var(--white);font-size:14px;display:flex;align-items:center;justify-content:center}
</style>
</head>
<body>
<header class="site-header abs">
  <div class="brand header-brand abs">
    <span class="brand-mark"></span>
    <span class="brand-name">SILVER TOUCH MASSAGE</span>
    <span class="brand-sub">MOBILE</span>
  </div>
  <div class="contact-item call abs">
    <svg viewBox="0 0 34 34"><circle cx="17" cy="17" r="15" fill="none" stroke="var(--green)" stroke-width="2"/><path d="M11 9c2-1 3 0 4 3l-2 2c1 3 3 5 6 6l2-2c3 1 4 2 3 4-1 2-3 3-6 2-5-2-8-5-10-10-1-3 0-4 3-5z" fill="var(--green)"/></svg>
    <div>Call Us:<br>0400 123 456</div>
  </div>
  <div class="contact-item mail abs">
    <svg viewBox="0 0 34 34"><rect x="4" y="8" width="26" height="18" fill="none" stroke="var(--green)" stroke-width="2.5"/><path d="M4 8l13 11 13-11" fill="none" stroke="var(--green)" stroke-width="2.5"/></svg>
    <div>Mail Us:<br>hello@silvertouchmm.com</div>
  </div>
  <nav class="nav main-nav abs">
    <a class="active" href="#">HOME</a>
    <a href="#">MASSAGE SERVICES</a>
    <a class="jp" href="#">ホーム</a>
    <a href="#">CONTACT US</a>
  </nav>
</header>

<section class="hero abs" role="img" aria-label="Therapist shaking hands with a senior client outside among tropical plants">
  <span class="hero-arrow prev abs"><svg width="12" height="18" viewBox="0 0 12 18"><path d="M10 1L2 9l8 8" fill="none" stroke="#999" stroke-width="2"/></svg></span>
  <span class="hero-arrow next abs"><svg width="12" height="18" viewBox="0 0 12 18"><path d="M2 1l8 8-8 8" fill="none" stroke="#999" stroke-width="2"/></svg></span>
  <p class="hero-caption abs">OUR BUSINESS IS A MOBILE MASSAGE<br>SERVICE FOR GOLD COAST SENIORS</p>
</section>

<div class="about-photo photo-one abs" role="img" aria-label="Therapist giving a seated chair massage to a client"></div>
<div class="about-photo photo-two abs" role="img" aria-label="Therapist holding the hand of a smiling senior client in an armchair"></div>

<section class="about abs">
  <h2 class="section-title">ABOUT <span>SILVER TOUCH MOBILE MASSAGE</span></h2>
  <p>Silver Touch Mobile Massage (STMM) is a mobile massage service for seniors living on the Gold Coast. We offer a variety of different massage treatments, including; relaxation, remedial, shiatsu and reflexology. Most of our clients are over 50's, however, we also provide massage services for all ages.</p>
  <h3>What does mobile massage mean?</h3>
  <p>Once you've made a booking with us by phone or email, we will arrange for a therapist to come directly to your house, business, facility or apartment. Our therapists bring all the required equipment directly to your place of residence. After you've received your amazing massage experience, our therapist will pack up and be on their way.</p>
  <p>STMM is focused on providing a comprehensive service that builds relationships between clients and massage therapists. We take time each session to listen to you and ensure that we understand any ailments, injuries or concerns that you would like us to be aware of. We also track each session with an electronic database to ensure continuity between sessions.</p>
  <p><strong>EFTPOS</strong> facilities are available for client convenience and gift vouchers can also be purchased.</p>
  <p>We invite you to take the time to explore our website as a source of information for learning about the art of massage therapy.</p>
  <p>If you would like more information on what massage can do for you, feel free to contact us, we'd love to help.</p>
  <a class="btn" href="#">READ MORE</a>
</section>

<section class="services abs">
  <h2 class="section-title">OUR <span>MASSAGE SERVICES</span></h2>
  <div class="title-rule abs"></div>
  <div class="service abs" style="left:73px">
    <div class="service-photo" role="img" aria-label="Senior woman receiving a relaxing face massage" style="background:radial-gradient(circle at 45% 55%,#e8c9b4,#c9a58c 60%,#f1ece6)"></div>
    <h3>Relaxation</h3>
    <p>A therapeutic massage style that focusses<br>on soft, gentle and relaxing strokes.</p>
    <a href="#">Read More</a>
  </div>
  <div class="service abs" style="left:334px">
    <div class="service-photo" role="img" aria-label="Man lying down receiving an oil back massage" style="background:radial-gradient(circle at 50% 55%,#d9a07a,#b57652 60%,#f3eee8)"></div>
    <h3>Remedial</h3>
    <p>An oil massage treatment that can<br>be gentle or strong, deep or shallow.</p>
    <a href="#">Read More</a>
  </div>
  <div class="service abs" style="left:596px">
    <div class="service-photo" role="img" aria-label="Therapist applying shiatsu pressure to a client on a table" style="background:linear-gradient(180deg,#e4ded6 0%,#2a2a2a 45%,#f5f5f5 75%)"></div>
    <h3>Shiatsu</h3>
    <p>Promotes energy flow by applying<br>pressure to tense and sore muscles,</p>
    <a href="#">Read More</a>
  </div>
  <div class="service abs" style="left:857px">
    <div class="service-photo" role="img" aria-label="Therapist massaging a client's foot for reflexology" style="background:linear-gradient(180deg,#9fd0dc 0%,#2a2a2a 45%,#e9c3ad 75%)"></div>
    <h3>Reflexology</h3>
    <p>Pressure is applied to the feet's reflexes<br>for a relaxing and relieving experience.</p>
    <a href="#">Read More</a>
  </div>
</section>

<footer class="site-footer abs">
  <div class="brand footer-brand abs">
    <span class="brand-mark"></span>
    <span class="brand-name">SILVER TOUCH MASSAGE</span>
    <span class="brand-sub">MOBILE</span>
  </div>
  <nav class="nav footer-nav abs">
    <a class="active" href="#">HOME</a>
    <a href="#">MASSAGE SERVICES</a>
    <a class="jp" href="#">ホーム</a>
    <a href="#">CONTACT US</a>
  </nav>
  <div class="socials abs">
    <span style="background:#3b5998"></span>
    <span style="background:#3fb3e8"></span>
    <span style="background:#f0851a"></span>
  </div>
</footer>
<div class="copyright abs">Copyright © 2017 Silvertouchmobilemassage. All Right Reserved.</div>
</body>
</html>
```